Palmcrest Shuttle & Excursions St. Lucia

I want a website design that is vibrant, engaging, and converts.
I plan on using Squarespace for hosting.

Target Market(s)

Tourists and visitors to St. Lucia; Focus: North American Market then European

Industry/Entity Type

Travel & Tourism

Coding

Coded - Design and coding required

Number of Pages Required

1 page

```html
<!DOCTYPE html>
<html lang="en">
<head>
<meta charset="utf-8">
<title>Palmcrest Shuttle &amp; Excursions St. Lucia</title>
<link href="https://fonts.googleapis.com/css2?family=Merriweather:wght@700;900&family=Roboto:wght@400;500;700&display=swap" rel="stylesheet">
<style>
:root{
  --navy:#1b2f6b;
  --green:#1eaf56;
  --blue:#1a9bd7;
  --ink:#222;
  --muted:#6b6b6b;
  --pale:#eef7fb;
  --white:#fff;
}
*{box-sizing:border-box;margin:0;padding:0}
html,body{width:1200px;height:4815px;overflow:hidden}
body{position:relative;background:var(--white);font-family:"Roboto",Arial,sans-serif;color:var(--ink)}
.abs{position:absolute}
.serif{font-family:"Merriweather",Georgia,serif;font-weight:700}
.btn{position:absolute;display:flex;align-items:center;justify-content:center;gap:8px;border-radius:24px;color:var(--white);font-size:13px;font-weight:700;letter-spacing:.2px;text-transform:uppercase}
.btn .dot{width:13px;height:13px;border-radius:50%;background:var(--white);display:inline-flex;align-items:center;justify-content:center}
.btn-green{background:var(--green)}
.btn-blue{background:var(--blue)}
.photo{position:absolute}

/* header */
.brand{left:114px;top:12px;color:var(--navy)}
.brand .name{font-size:25px;line-height:30px;letter-spacing:.2px}
.brand .tag{font-size:13px;line-height:18px}
.contact-chip{display:flex;align-items:center;gap:14px;top:18px}
.chip-icon{width:44px;height:44px;border-radius:50%;background:var(--green);display:flex;align-items:center;justify-content:center}
.chip-label{font-size:12px;color:var(--muted)}
.chip-value{font-size:16px;font-weight:500;color:var(--ink);margin-top:3px}
.main-nav{left:0;top:80px;width:1200px;height:44px;background:var(--navy);color:var(--white);font-size:14px}
.main-nav span{position:absolute;top:14px}

/* hero */
.hero{left:0;top:124px;width:1200px;height:726px;background:linear-gradient(180deg,#3fa6c9 0%,#8fcbe0 28%,#6f8aa0 48%,#8e8a6a 66%,#7a6a3a 100%)}
.hero-title{left:0;top:414px;width:1200px;text-align:center;color:var(--white);font-size:54px;line-height:68px;text-shadow:0 2px 6px rgba(0,0,0,.35)}
.slider-arrow{width:34px;height:34px;border-radius:50%;border:2px solid var(--white);display:flex;align-items:center;justify-content:center}

/* section heading */
.sec-title{left:0;width:1200px;text-align:center;font-size:38px;line-height:46px}

/* about */
.about-title{left:613px;top:972px;color:var(--navy);font-size:36px}
.about-text{left:613px;width:476px;font-size:14px;line-height:25.5px;color:var(--muted);text-align:justify}

/* services */
.services{left:0;top:1441px;width:1200px;height:777px;background:var(--pale)}
.card{position:absolute;width:308px;height:460px;background:var(--white);border-radius:10px;box-shadow:0 4px 14px rgba(0,0,0,.15)}
.card .img{position:absolute;left:6px;top:6px;width:296px;height:214px;border-radius:6px}
.card h3{position:absolute;top:248px;width:100%;text-align:center;font-size:17px;font-weight:700}
.card p{position:absolute;top:284px;left:18px;width:272px;text-align:center;font-size:13.5px;line-height:24px;color:var(--muted)}
.card .btn{left:87px;top:380px;width:145px;height:40px}
.chev{font-size:22px;color:var(--ink)}

/* gallery */
.dots span{position:absolute;top:2938px;width:20px;height:20px;border-radius:50%;background:#cfcfcf}

/* testimonial */
.testimonials{left:0;top:3049px;width:1200px;height:556px;background:var(--green)}
.quote-card{position:absolute;top:3250px;width:409px;height:230px;background:var(--white);border-radius:30px;box-shadow:0 4px 14px rgba(0,0,0,.15)}
.quote-card .avatar{position:absolute;left:-55px;top:57px;width:114px;height:114px;border-radius:50%;border:4px solid var(--white)}
.quote-card .qmark{position:absolute;left:100px;top:14px;font-size:64px;line-height:64px;color:var(--navy)}
.quote-card p{position:absolute;left:100px;top:78px;width:280px;font-size:13px;line-height:24px;color:var(--muted)}
.quote-card .who{position:absolute;left:100px;top:153px;font-size:16px;font-weight:700}
.quote-card .stars{position:absolute;left:100px;top:180px;color:#f5a623;font-size:18px;letter-spacing:2px}

/* contact */
.contact-panel{left:462px;top:3761px;width:624px;height:433px;background:var(--white);box-shadow:0 6px 24px rgba(0,0,0,.12)}
.field-label{position:absolute;font-size:14px;font-weight:700}
.field-value{position:absolute;font-size:12px;color:#8a8a8a}
.field-line{position:absolute;height:1px;background:#cfcfcf}

/* footer */
.footer{left:0;top:4370px;width:1200px;height:445px;background:var(--navy);color:var(--white)}
.foot-head{font-size:16px;font-weight:700}
.foot-link{position:absolute;font-size:14px}
.foot-link::before{content:"»";margin-right:8px}
.social{position:absolute;top:4575px;width:34px;height:34px;border-radius:50%;background:var(--white);display:flex;align-items:center;justify-content:center}
</style>
</head>
<body>

<!-- Header -->
<div class="abs brand serif">
  <div class="name">PALMCREST SHUTTLE</div>
  <div class="tag">&amp; EXCURSIONS ST. LUCIA</div>
</div>

<div class="abs contact-chip" style="left:460px">
  <div class="chip-icon"><svg width="18" height="18" viewBox="0 0 24 24"><path fill="#fff" d="M6.6 10.8a15.1 15.1 0 0 0 6.6 6.6l2.2-2.2a1 1 0 0 1 1-.25 11.4 11.4 0 0 0 3.6.57 1 1 0 0 1 1 1V20a1 1 0 0 1-1 1A17 17 0 0 1 3 4a1 1 0 0 1 1-1h3.5a1 1 0 0 1 1 1c0 1.25.2 2.45.57 3.57a1 1 0 0 1-.25 1z"/></svg></div>
  <div><div class="chip-label">Call Us Today</div><div class="chip-value">+1 758 555 0142</div></div>
</div>
<div class="abs contact-chip" style="left:671px">
  <div class="chip-icon"><svg width="18" height="18" viewBox="0 0 24 24"><path fill="#fff" d="M2 5h20v14H2z"/><path d="M2 5l10 8 10-8" fill="none" stroke="#1eaf56" stroke-width="2"/></svg></div>
  <div><div class="chip-label">Email Us Today</div><div class="chip-value" style="font-size:15px">info@palmcrestlc.com</div></div>
</div>
<div class="btn btn-blue" style="left:914px;top:15px;width:172px;height:47px">Book a Tour <span class="dot"><svg width="7" height="7" viewBox="0 0 10 10"><path d="M3 1l4 4-4 4" stroke="#1a9bd7" stroke-width="2" fill="none"/></svg></span></div>

<nav class="abs main-nav">
  <span style="left:172px">HOME</span><span style="left:241px">|</span>
  <span style="left:273px">ABOUT US</span><span style="left:372px">|</span>
  <span style="left:406px">TOURS</span><span style="left:482px">|</span>
  <span style="left:512px">TRANSPORTS</span><span style="left:636px">|</span>
  <span style="left:665px">GALLERY</span><span style="left:783px">|</span>
  <span style="left:813px">REVIEWS</span><span style="left:905px">|</span>
  <span style="left:934px">CONTACT US</span>
</nav>

<!-- Hero -->
<div class="photo hero" role="img" aria-label="Two hikers jumping with joy on a grassy mountain top under a blue sky"></div>
<h1 class="abs hero-title serif">PALMCREST SHUTTLE &amp;<br>EXCURSIONS ST. LUCIA.</h1>
<div class="btn btn-green" style="left:525px;top:577px;width:183px;height:49px;font-size:15px">Get a Quote <span class="dot"><svg width="7" height="7" viewBox="0 0 10 10"><path d="M3 1l4 4-4 4" stroke="#1eaf56" stroke-width="2" fill="none"/></svg></span></div>
<div class="abs slider-arrow" style="left:37px;top:512px"><svg width="12" height="12" viewBox="0 0 10 10"><path d="M7 1L3 5l4 4" stroke="#fff" stroke-width="1.5" fill="none"/></svg></div>
<div class="abs slider-arrow" style="left:1129px;top:512px"><svg width="12" height="12" viewBox="0 0 10 10"><path d="M3 1l4 4-4 4" stroke="#fff" stroke-width="1.5" fill="none"/></svg></div>
<svg class="abs" style="left:0;top:760px" width="1200" height="91" viewBox="0 0 1200 91" preserveAspectRatio="none">
  <path d="M0 40 Q300 10 600 40 T1200 30 V91 H0Z" fill="#fff"/>
</svg>

<!-- About -->
<div class="photo" role="img" aria-label="Two surfers running into the sea carrying surfboards" style="left:125px;top:945px;width:416px;height:416px;border-radius:50%;background:linear-gradient(160deg,#7fb4c9,#2f6f8a 55%,#cfe3ea);border:6px solid var(--green);box-shadow:inset 0 0 0 4px var(--blue)"></div>
<h2 class="abs about-title serif">ABOUT US</h2>
<p class="abs about-text" style="top:1031px">Lorem ipsum dolor sit amet, consectetur adipiscing elit, sed do eiusmod tempor incididunt ut labore et dolore magna aliqua. Ut enim ad minim veniam, quis nostrud exercitation ullamco laboris nisi ut aliquip commodo consequat. Duis aute irure dolor in reprehenderit in voluptate velit esse cillum dolore eu fugiat nulla pariatur.</p>
<p class="abs about-text" style="top:1170px">Sed ut perspiciatis unde omnis iste natus error sit voluptatem accusantium doloremque laudantium, totam rem aperiam, eaque ipsa quae ab illo inventore veritatis et quasi architecto explicabo.</p>
<div class="btn btn-green" style="left:613px;top:1273px;width:211px;height:45px">Learn More About <span class="dot"><svg width="7" height="7" viewBox="0 0 10 10"><path d="M3 1l4 4-4 4" stroke="#1eaf56" stroke-width="2" fill="none"/></svg></span></div>

<!-- Services -->
<section class="abs services"></section>
<h2 class="abs sec-title serif" style="top:1518px;color:var(--navy)">ST LUCIA AIRPORT TRANSFERS</h2>
<h2 class="abs sec-title serif" style="top:1563px;color:var(--green)">SERVICES WE OFFER</h2>
<span class="abs chev" style="left:57px;top:1871px">‹</span>
<span class="abs chev" style="left:1128px;top:1871px">›</span>

<div class="card" style="left:112px;top:1656px">
  <div class="photo img" role="img" aria-label="Riders on quad bikes on a forest trail" style="background:linear-gradient(160deg,#6b8a3a,#a06a3a 60%,#4a3a2a)"></div>
  <h3>Lorem ipsum dolor sit amet</h3>
  <p>Sed ut perspiciatis unde omnis iste natus sit voluptatem accusantium doloremque laudantium, totam aperiam,</p>
  <div class="btn btn-blue">Learn More <span class="dot"><svg width="7" height="7" viewBox="0 0 10 10"><path d="M3 1l4 4-4 4" stroke="#1a9bd7" stroke-width="2" fill="none"/></svg></span></div>
</div>
<div class="card" style="left:445px;top:1671px">
  <div class="photo img" role="img" aria-label="Woman gliding on a zipline through the forest canopy" style="background:linear-gradient(160deg,#2d5a4a,#3f7a5f 55%,#1c3a33)"></div>
  <h3>Lorem ipsum dolor sit amet</h3>
  <p>Sed ut perspiciatis unde omnis iste natus sit voluptatem accusantium doloremque laudantium, totam aperiam,</p>
  <div class="btn btn-blue" style="left:82px">Learn More <span class="dot"><svg width="7" height="7" viewBox="0 0 10 10"><path d="M3 1l4 4-4 4" stroke="#1a9bd7" stroke-width="2" fill="none"/></svg></span></div>
</div>
<div class="card" style="left:779px;top:1656px">
  <div class="photo img" role="img" aria-label="Friends jumping from a boat into the sea" style="background:linear-gradient(160deg,#c9d6dc,#9aa8ad 55%,#5a6c72)"></div>
  <h3>Lorem ipsum dolor sit amet</h3>
  <p>Sed ut perspiciatis unde omnis iste natus sit voluptatem accusantium doloremque laudantium, totam aperiam,</p>
  <div class="btn btn-blue">Learn More <span class="dot"><svg width="7" height="7" viewBox="0 0 10 10"><path d="M3 1l4 4-4 4" stroke="#1a9bd7" stroke-width="2" fill="none"/></svg></span></div>
</div>

<!-- Gallery -->
<h2 class="abs sec-title serif" style="top:2308px"><span style="color:var(--navy)">OUR</span> <span style="color:var(--green)">GALLERY</span></h2>
<div class="photo" role="img" aria-label="Friends relaxing on a longtail boat in a turquoise lagoon" style="left:110px;top:2391px;width:307px;height:248px;background:linear-gradient(170deg,#4f7a5a,#3bbcbc 50%,#8a6a4a)"></div>
<div class="photo" role="img" aria-label="Happy traveller leaning out of a car window" style="left:426px;top:2391px;width:344px;height:248px;background:linear-gradient(120deg,#5c6e3a,#c9a070 55%,#3a3a3a)"></div>
<div class="photo" role="img" aria-label="People paddling a kayak on a river" style="left:783px;top:2391px;width:307px;height:248px;background:linear-gradient(160deg,#3a4a3a,#5a6a6a 55%,#2a3a4a)"></div>
<div class="photo" role="img" aria-label="Off-road vehicle in snowy mountains" style="left:110px;top:2650px;width:307px;height:249px;background:linear-gradient(160deg,#6f8fa6,#cfc7c0 50%,#8a6a5a)"></div>
<div class="photo" role="img" aria-label="Hiker sitting on rocks above a mountain lake" style="left:426px;top:2650px;width:307px;height:249px;background:linear-gradient(160deg,#3a5a6a,#2f6f7a 55%,#1f2f3a)"></div>
<div class="photo" role="img" aria-label="Scuba diver over a colourful coral reef" style="left:744px;top:2650px;width:346px;height:249px;background:linear-gradient(160deg,#1ea0d8,#0f6fb0 60%,#c0603a)"></div>
<div class="dots">
  <span style="left:554px"></span><span style="left:577px"></span>
  <span style="left:601px;background:#fff;border:2px solid var(--green)"></span>
  <span style="left:625px"></span>
</div>
<div class="abs" style="left:607px;top:2944px;width:8px;height:8px;border-radius:50%;background:var(--green)"></div>

<!-- Testimonials -->
<section class="abs testimonials" role="img" aria-label="Green tinted backdrop of people kayaking"></section>
<h2 class="abs sec-title serif" style="top:3164px;color:var(--white)">CLIENT TESTIMONIAL</h2>
<svg class="abs" style="left:40px;top:3346px" width="24" height="36" viewBox="0 0 24 36"><path d="M18 3L5 18l13 15" stroke="#fff" stroke-width="4" fill="none"/></svg>
<svg class="abs" style="left:1136px;top:3346px" width="24" height="36" viewBox="0 0 24 36"><path d="M6 3l13 15L6 33" stroke="#fff" stroke-width="4" fill="none"/></svg>

<div class="quote-card" style="left:164px">
  <div class="photo avatar" role="img" aria-label="Portrait of a smiling client" style="background:linear-gradient(160deg,#c98a4a,#6a3a2a)"></div>
  <div class="qmark serif">“</div>
  <p>Lorem ipsum dolor sit amet, consectetur adipiscing elit, sed do eiusmod tempor incididunt ut magna aliqua.</p>
  <div class="who">John Doe</div>
  <div class="stars">★★★★★</div>
</div>
<div class="quote-card" style="left:678px">
  <div class="photo avatar" role="img" aria-label="Portrait of a smiling client in a sun hat" style="background:linear-gradient(160deg,#e0b070,#8a5a3a)"></div>
  <div class="qmark serif">“</div>
  <p>Lorem ipsum dolor sit amet, consectetur adipiscing elit, sed do eiusmod tempor incididunt ut magna aliqua.</p>
  <div class="who">John Doe</div>
  <div class="stars">★★★★★</div>
</div>

<!-- Contact -->
<div class="photo" role="img" aria-label="Blue tinted photo of travellers" style="left:108px;top:3710px;width:449px;height:383px;background:linear-gradient(160deg,#1ba3d6,#1592c4)"></div>
<div class="abs" style="left:108px;top:3814px;width:309px;text-align:right;color:var(--white);font-size:16px;font-weight:500">CONTACT US</div>
<div class="abs serif" style="left:108px;top:3858px;width:309px;text-align:right;color:var(--white);font-size:36px;line-height:44px">Let’s Do<br>Good<br>Together!</div>
<div class="abs" style="left:742px;top:3729px;width:365px;height:346px;border:4px solid var(--navy)"></div>

<div class="abs contact-panel">
  <h2 class="abs serif" style="left:52px;top:30px;font-size:36px;color:var(--ink)">CONTACT US</h2>
  <span class="field-label" style="left:56px;top:110px">Your Name</span>
  <span class="field-value" style="left:56px;top:140px">John Smith</span>
  <span class="field-line" style="left:56px;top:164px;width:228px"></span>
  <span class="field-label" style="left:332px;top:110px">Company</span>
  <span class="field-value" style="left:332px;top:140px">Lorem ipsum dolor sit amet</span>
  <span class="field-line" style="left:332px;top:164px;width:228px"></span>
  <span class="field-label" style="left:56px;top:202px">Email Address</span>
  <span class="field-value" style="left:56px;top:233px">johnsmith@example.com</span>
  <span class="field-line" style="left:56px;top:257px;width:228px"></span>
  <span class="field-label" style="left:332px;top:202px">Phone</span>
  <span class="field-value" style="left:332px;top:233px">01122-123-456-789</span>
  <span class="field-line" style="left:332px;top:257px;width:228px"></span>
  <span class="field-label" style="left:56px;top:296px">Message</span>
  <span class="field-value" style="left:56px;top:327px">Hi, do you have a moment to talk abo...|</span>
  <span class="field-line" style="left:56px;top:379px;width:480px"></span>
  <div class="abs" style="left:500px;top:323px;width:64px;height:64px;border-radius:50%;background:var(--green);display:flex;align-items:center;justify-content:center">
    <svg width="22" height="22" viewBox="0 0 24 24"><path d="M22 2L2 10l8 3 3 8z" fill="#fff"/></svg>
  </div>
</div>

<!-- Footer -->
<svg class="abs" style="left:0;top:4300px" width="1200" height="72" viewBox="0 0 1200 72" preserveAspectRatio="none">
  <path d="M0 40 Q300 10 600 36 T1200 30 V72 H0Z" fill="#1b2f6b"/>
</svg>
<footer class="abs footer"></footer>
<div class="abs serif" style="left:78px;top:4488px;width:330px;text-align:center;color:var(--white)">
  <div style="font-size:26px;line-height:32px">PALMCREST SHUTTLE</div>
  <div style="font-size:13px;line-height:18px">&amp; EXCURSIONS ST. LUCIA</div>
</div>
<span class="social" style="left:161px" aria-label="Share"><svg width="16" height="16" viewBox="0 0 16 16"><circle cx="4" cy="8" r="2" fill="#1b2f6b"/><circle cx="12" cy="3.5" r="2" fill="#1b2f6b"/><circle cx="12" cy="12.5" r="2" fill="#1b2f6b"/><path d="M4 8l8-4.5M4 8l8 4.5" stroke="#1b2f6b" stroke-width="1.4"/></svg></span>
<span class="social" style="left:204px" aria-label="Email"><svg width="16" height="12" viewBox="0 0 16 12"><rect x=".75" y=".75" width="14.5" height="10.5" fill="none" stroke="#1b2f6b" stroke-width="1.5"/><path d="M1 1l7 5 7-5" fill="none" stroke="#1b2f6b" stroke-width="1.5"/></svg></span>
<span class="social" style="left:247px" aria-label="Website"><svg width="16" height="16" viewBox="0 0 16 16"><circle cx="8" cy="8" r="6.5" fill="none" stroke="#1b2f6b" stroke-width="1.4"/><path d="M1.5 8h13M8 1.5c-2.5 3-2.5 10 0 13M8 1.5c2.5 3 2.5 10 0 13" fill="none" stroke="#1b2f6b" stroke-width="1.2"/></svg></span>
<span class="social" style="left:290px" aria-label="Phone"><svg width="14" height="14" viewBox="0 0 24 24"><path fill="#1b2f6b" d="M6.6 10.8a15.1 15.1 0 0 0 6.6 6.6l2.2-2.2a1 1 0 0 1 1-.25 11.4 11.4 0 0 0 3.6.57 1 1 0 0 1 1 1V20a1 1 0 0 1-1 1A17 17 0 0 1 3 4a1 1 0 0 1 1-1h3.5a1 1 0 0 1 1 1c0 1.25.2 2.45.57 3.57a1 1 0 0 1-.25 1z"/></svg></span>

<div class="abs foot-head" style="left:435px;top:4462px;color:#fff">Quick Links</div>
<span class="foot-link" style="left:435px;top:4500px;color:#fff">Home</span>
<span class="foot-link" style="left:435px;top:4532px;color:#fff">About Us</span>
<span class="foot-link" style="left:435px;top:4565px;color:#fff">Tours</span>
<span class="foot-link" style="left:435px;top:4598px;color:#fff">Transports</span>
<span class="foot-link" style="left:435px;top:4631px;color:#fff">Gallery</span>
<span class="foot-link" style="left:435px;top:4663px;color:#fff">Reviews</span>
<span class="foot-link" style="left:435px;top:4695px;color:#fff">Contact Us</span>

<div class="abs foot-head" style="left:632px;top:4462px;color:#fff">Important</div>
<span class="foot-link" style="left:632px;top:4502px;color:#fff">Terms of Use</span>
<span class="foot-link" style="left:632px;top:4534px;color:#fff">Site Map</span>
<span class="foot-link" style="left:632px;top:4567px;color:#fff">Privacy Policy</span>
<span class="foot-link" style="left:632px;top:4600px;color:#fff">Disclaimer</span>
<span class="foot-link" style="left:632px;top:4632px;color:#fff">Support</span>

<div class="abs foot-head" style="left:837px;top:4462px;color:#fff">Contact us</div>
<svg class="abs" style="left:837px;top:4506px" width="12" height="16" viewBox="0 0 12 16"><path d="M6 0a6 6 0 0 0-6 6c0 4.5 6 10 6 10s6-5.5 6-10a6 6 0 0 0-6-6zm0 8.5A2.5 2.5 0 1 1 6 3.5a2.5 2.5 0 0 1 0 5z" fill="#fff"/></svg>
<div class="abs" style="left:867px;top:4504px;color:#fff;font-size:14px;line-height:24px">1-294 Lorem ipsum dolor sit<br>consectetur adipiscing</div>
<svg class="abs" style="left:836px;top:4568px" width="14" height="14" viewBox="0 0 24 24"><path fill="#fff" d="M6.6 10.8a15.1 15.1 0 0 0 6.6 6.6l2.2-2.2a1 1 0 0 1 1-.25 11.4 11.4 0 0 0 3.6.57 1 1 0 0 1 1 1V20a1 1 0 0 1-1 1A17 17 0 0 1 3 4a1 1 0 0 1 1-1h3.5a1 1 0 0 1 1 1c0 1.25.2 2.45.57 3.57a1 1 0 0 1-.25 1z"/></svg>
<div class="abs" style="left:867px;top:4566px;color:#fff;font-size:14px">+1 758 555 0142</div>
<svg class="abs" style="left:836px;top:4613px" width="15" height="14" viewBox="0 0 15 14"><rect x="1" y="4" width="13" height="8" rx="1" fill="#fff"/><rect x="4" y="0" width="7" height="5" fill="#fff"/></svg>
<div class="abs" style="left:867px;top:4612px;color:#fff;font-size:14px">+1 758 555 0199</div>
<svg class="abs" style="left:836px;top:4660px" width="15" height="12" viewBox="0 0 15 12"><rect x=".75" y=".75" width="13.5" height="10.5" fill="none" stroke="#fff" stroke-width="1.5"/><path d="M1 1l6.5 5L14 1" fill="none" stroke="#fff" stroke-width="1.5"/></svg>
<div class="abs" style="left:873px;top:4657px;color:#fff;font-size:14px">info@palmcrestlc.com</div>

<div class="abs" style="left:0;top:4742px;width:1200px;height:1px;background:rgba(255,255,255,.25)"></div>
<div class="abs" style="left:0;top:4767px;width:1200px;text-align:center;color:#fff;font-size:13px">© 2023 Palmcrest Shuttle &amp; Excursions St. Lucia | All Rights Reserved</div>

<div class="abs" style="left:1121px;top:4673px;width:34px;height:34px;border-radius:50%;background:var(--green);display:flex;align-items:center;justify-content:center">
  <svg width="16" height="14" viewBox="0 0 16 14"><path d="M2 1h12a1 1 0 0 1 1 1v7a1 1 0 0 1-1 1H7l-4 3v-3H2a1 1 0 0 1-1-1V2a1 1 0 0 1 1-1z" fill="#fff"/></svg>
</div>

</body>
</html>
```